Business card and company logo design needed

Need a business card and company logo design for all stationary for an Aviation refueling consultancy business. Our business offers consulting services in the specialist aviation refueling industry. Services range from engineering, compliance and management consultancy through to project management services. This encompasses infrastructure from refinery through to airport and into the aircraft wing.

Design should be simple, 'less-is-more' concept, possibly taking advantage of the 'm' for tevlon and the fact is it the aviation industry. It should convey confidence, safety, experience, professionalism, aviation, engineering?, and should not be afraid to be simple in color...though please do not let this restrict your designs and imagination.

Target Market(s)

Airport authorities, oil majors, aircraft operators

Industry/Entity Type

Airport

Contact Information for Business Card

Tevlon Skyward Advisory Pty Ltd
Darius Tevlon
Director
mobile:+61427305158
email: darius@tevlonadvisory.example
Skype: darius.tevlonadvisory

Logo styles of interest
Emblem Logo
Pictorial/Combination Logo
Abstract Logo
Wordmark Logo
Lettermark Logo
Requirements
Must have
• - A feel of safety, security and confidence
Nice to have
• - Aviation has both heritage and modern 'sexy' elements so would be nice to try and capture both
- Aviation 'JET' fuel color is designated as black in signage or labels
- Themes? : Aviation fuel is derived from oil, it burns, safety, Jet fuel is colorless
- Company is global in reach, borderless like aircraft
Should not have
• - Cliche:

```html
<!DOCTYPE html>
<html lang="en">
<head>
<meta charset="utf-8">
<title>Tevlon Skyward Advisory – Business Card</title>
<link rel="stylesheet" href="https://fonts.googleapis.com/css2?family=Bebas+Neue&display=swap">
<style>
  :root {
    --backdrop: #e4e1dd;
    --card: #f7f7f7;
    --card-shade: #ececec;
    --brand-blue: #2bb3e3;
    --bar-dark: #3a3b3d;
    --bar-text: #ffffff;
    --dot-blue: #8fd2ee;
  }
  * { box-sizing: border-box; margin: 0; padding: 0; }
  html, body {
    width: 849px; height: 1200px; overflow: hidden;
    background: var(--backdrop);
    font-family: "Bebas Neue", "Arial Narrow", sans-serif;
  }
  .canvas {
    position: relative; width: 849px; height: 1200px;
  }
  .card {
    position: absolute; left: 74px; width: 700px; height: 400px;
    background: linear-gradient(135deg, var(--card) 0%, var(--card-shade) 100%);
    box-shadow: 0 6px 18px rgba(0,0,0,0.18);
    overflow: hidden;
  }
  .card--front { top: 150px; }
  .card--back { top: 650px; }

  .texture {
    position: absolute; inset: 0;
    background: linear-gradient(160deg, rgba(255,255,255,0.6) 0%, rgba(225,228,232,0.5) 100%);
  }

  .wordmark {
    position: absolute; color: var(--brand-blue);
    line-height: 0.95; letter-spacing: 1px;
  }
  .card--front .wordmark { left: 52px; top: 52px; font-size: 40px; }
  .card--back .wordmark {
    left: 0; right: 0; top: 140px; text-align: center; font-size: 64px;
  }
  .wordmark .line { display: block; }
  .wordmark .line--sub { font-size: 0.55em; letter-spacing: 4px; margin-top: 4px; }

  .dots { position: absolute; display: flex; gap: 12px; }
  .dots span { width: 9px; height: 9px; border-radius: 50%; background: var(--dot-blue); }
  .card--front .dots { left: 30px; top: 190px; }
  .card--back .dots { left: 296px; top: 300px; }

  .contact {
    position: absolute; right: 0; top: 190px;
    display: flex; flex-direction: column; align-items: flex-end; gap: 6px;
  }
  .contact .bar {
    background: var(--bar-dark); color: var(--bar-text);
    font-size: 21px; letter-spacing: 1px;
    height: 30px; line-height: 30px; padding: 0 28px 0 16px;
  }
  .contact .bar--name { width: 300px; }
  .contact .bar--phone { width: 330px; }
  .contact .bar--email { width: 360px; }
  .contact .bar--skype { width: 390px; }
</style>
</head>
<body>
<main class="canvas">

  <section class="card card--front" aria-label="Business card front">
    <div class="texture" role="img" aria-label="Fine light diagonal stripe texture"></div>
    <div class="wordmark">
      <span class="line">Tevlon Skyward</span>
      <span class="line line--sub">Advisory Pty Ltd</span>
    </div>
    <div class="dots"><span></span><span></span></div>
    <div class="contact">
      <p class="bar bar--name">Darius Tevlon Director</p>
      <p class="bar bar--phone">+61427305158</p>
      <p class="bar bar--email">darius@tevlonadvisory.example</p>
      <p class="bar bar--skype">Skype: darius.tevlonadvisory</p>
    </div>
  </section>

  <section class="card card--back" aria-label="Business card back">
    <div class="texture" role="img" aria-label="Fine light diagonal stripe texture"></div>
    <div class="wordmark">
      <span class="line">Tevlon Skyward</span>
      <span class="line line--sub">Advisory Pty Ltd</span>
    </div>
    <div class="dots"><span></span><span></span></div>
  </section>

</main>
</body>
</html>
```